Wordpress Fashion Website

Please see attached:
1) Our detailed design document.
2) Velvet Lane Wardrobe logo.
3) 20 images to be used as tiles in the homepage design.
Of importance to us is:
1) That our 'Unique Selling Point' of selling fashion based on your preferred style is immediately understood by the user.
2) The site is very aesthetically pleasing and appeals to the fashion conscious woman.
3) Clean design and SEO friendly.
4) Some of the style tiles can be seen in the homepage screenshot.
The design specification document should be used as a guideline. Please use your creativity and expertise to deviate from this as you wish. We look forward to seeing your submissions!
Gareth
Updates
We very much like this design and would welcome submissions along these lines also: http://www.kemrolu.qc.ca/fr/ Added Friday, December 19, 2014
Industry/Entity Type
Fashion
Look and feel
Each slider illustrates characteristics of the customer's brand and the style your logo design should communicate.

```html
<!DOCTYPE html>
<html lang="en">
<head>
<meta charset="utf-8">
<title>Velvet Lane Wardrobe — Shop by Style</title>
<link href="https://fonts.googleapis.com/css2?family=Raleway:wght@300;400;500;600&display=swap" rel="stylesheet">
<style>
:root{
  --green:#1fa37a;
  --black:#0c0c0c;
  --ink:#222;
  --muted:#777;
  --line:#e3e3e3;
  --band:#f1f1f1;
  --white:#fff;
  --panel:#1b1b1b;
  --gray-tile:#dcdcdc;
}
*{margin:0;padding:0;box-sizing:border-box}
html,body{width:1200px;height:3557px;overflow:hidden}
body{position:relative;background:var(--white);font-family:"Raleway",Arial,sans-serif;color:var(--ink)}
.abs{position:absolute}

/* sidebar */
.sidebar{left:0;top:0;width:183px;height:3557px;background:var(--white);border-right:1px solid var(--line)}
.brand{position:absolute;left:18px;top:18px;width:150px;font-weight:500;color:var(--ink);text-transform:uppercase;line-height:1.1}
.brand .name{font-size:17px;letter-spacing:1px;display:block}
.brand .sub{font-size:9px;letter-spacing:4px;display:block;margin-top:4px}
.side-nav{position:absolute;left:0;top:78px;width:183px;list-style:none}
.side-nav li{height:39px;line-height:39px;padding-left:32px;font-size:11px;text-transform:uppercase;color:#444;border-bottom:1px solid var(--line)}
.side-nav li.current{color:var(--green)}

/* top bar */
.topbar{left:183px;top:0;width:1017px;height:66px;background:var(--black)}
.search-input{left:208px;top:14px;width:337px;height:36px;border:1px solid #3a3a3a;background:#141414;color:#888;font-size:10px;line-height:34px;padding-left:14px}
.search-input .caret{position:absolute;right:12px;top:0;color:#777;font-size:9px}
.search-btn{left:562px;top:14px;width:83px;height:36px;border:2px solid var(--green);color:var(--green);font-size:10px;font-weight:600;text-align:center;line-height:32px}
.account-links{right:148px;top:0;line-height:66px;color:#ddd;font-size:10px;white-space:nowrap;display:flex;gap:6px}
.account-links .sep{color:#888}
.social-top{left:882px;top:21px;display:flex;gap:6px}
.dot{width:23px;height:23px;border-radius:50%;background:var(--white)}

/* hero */
.hero{left:183px;top:66px;width:1017px;height:432px;background:linear-gradient(100deg,#3a2e28 0%,#6b5a4c 22%,#b9b3ad 45%,#d8d6d3 70%,#cfcdca 100%)}
.style-finder{left:863px;top:173px;width:311px;height:178px;background:var(--panel)}
.style-finder .head{height:50px;background:var(--green);color:var(--white);font-size:18px;line-height:50px;padding-left:22px;letter-spacing:.5px}
.style-finder .label{position:absolute;left:24px;top:74px;color:var(--white);font-size:15px;letter-spacing:.5px}
.style-finder .select{position:absolute;left:24px;top:107px;width:258px;height:40px;background:var(--white);color:#666;font-size:10px;line-height:40px;padding-left:12px}
.style-finder .select .caret{position:absolute;right:12px;top:0;color:#222}
.slider-dots{left:1140px;top:463px;display:flex;gap:6px}
.slider-dots span{width:9px;height:9px;border-radius:50%;background:rgba(255,255,255,.6)}
.slider-dots span.on{background:var(--white)}

/* brands */
.brands{left:183px;top:498px;width:1017px;height:95px;background:var(--band);display:flex;align-items:center}
.brands .title{margin-left:28px;font-size:17px;color:#333;letter-spacing:.5px;width:150px}
.brands ul{list-style:none;display:flex;gap:0;width:820px;justify-content:space-between;padding-right:20px}
.brands li{font-size:18px;font-weight:600;color:#a9a9a9;text-transform:uppercase;letter-spacing:1px}

/* tiles */
.tile{position:absolute;overflow:hidden}
.tile .ph{position:absolute;inset:0}
.lbl{position:absolute;font-weight:300;text-transform:uppercase;font-size:19px;line-height:1.25;letter-spacing:.5px}
.lbl.sm{font-size:14px}
.light{color:var(--white)}
.dark{color:#444}
.vert{font-size:24px;line-height:1.25;text-align:center;width:30px;letter-spacing:0}
.chic-mark{position:absolute;left:50%;top:90px;transform:translateX(-50%);text-align:center;color:var(--white)}
.chic-mark .disc{width:120px;height:120px;border-radius:50%;background:var(--white);margin:0 auto 18px}
.overlay{position:absolute;inset:0;background:rgba(20,20,20,.55)}
.zoom{position:absolute;width:64px;height:64px;border-radius:50%;background:var(--green)}

/* promo row */
.promo-editors{left:183px;top:3040px;width:370px;height:266px;background:var(--black);color:var(--white);font-size:72px;font-weight:300;line-height:1.15;text-align:center;padding-top:44px;text-transform:uppercase}
.promo-specials{left:553px;top:3040px;width:367px;height:266px;background:var(--gray-tile);color:var(--green);font-size:62px;font-weight:300;text-align:center;line-height:266px;text-transform:uppercase}
.about{left:920px;top:3040px;width:280px;height:266px;background:var(--white);text-align:center}
.about .disc{width:56px;height:56px;border-radius:50%;background:var(--black);margin:16px auto 8px}
.about .name{font-size:13px;font-weight:600;text-transform:uppercase;letter-spacing:1px}
.about h3{font-size:17px;font-weight:400;text-transform:uppercase;margin-top:12px;letter-spacing:.5px}
.about p{font-size:11px;color:#555;line-height:1.45;margin:10px 34px 0}

/* footer */
.footer{left:183px;top:3306px;width:1017px;height:251px;background:var(--black);color:#bbb}
.fcol{position:absolute;top:36px}
.fcol h4{font-size:14px;font-weight:400;color:var(--green);text-transform:uppercase;letter-spacing:1px;margin-bottom:12px}
.fcol ul{list-style:none}
.fcol li{font-size:10px;line-height:19px;text-transform:capitalize}
.fcol li::before{content:"▪";color:#888;font-size:7px;margin-right:8px;vertical-align:2px}
.contact li::before{content:none}
.contact li{display:flex;align-items:center;gap:10px;line-height:15px;margin-bottom:10px}
.contact svg{flex:none}
.copyright{left:66px;top:212px;font-size:9px;color:#888}
.social-foot{left:855px;top:207px;display:flex;gap:7px}
.social-foot span{width:17px;height:17px;background:#2d7fc1}
.social-foot span.red{background:#c8312f}
</style>
</head>
<body>

<aside class="sidebar abs">
  <div class="brand"><span class="name">Velvet Lane</span><span class="sub">Wardrobe</span></div>
  <ul class="side-nav">
    <li class="current">Home</li>
    <li>Blog</li>
    <li>About</li>
    <li>Editors Pick</li>
    <li>Specials</li>
    <li>My Wardrobe</li>
  </ul>
</aside>

<header class="topbar abs">
  <div class="search-input abs">A keyword enter here<span class="caret">▼</span></div>
  <div class="search-btn abs">SEARCH</div>
  <div class="account-links abs"><span>LOG IN</span><span class="sep">|</span><span>SIGN UP</span><span class="sep">|</span><span>SOCIAL MEDIA</span></div>
  <div class="social-top abs"><span class="dot"></span><span class="dot"></span><span class="dot"></span><span class="dot"></span></div>
</header>

<section class="hero abs" role="img" aria-label="Hero photo: woman with long wavy hair in a leather jacket and blue jeans in front of a pale building"></section>
<div class="style-finder abs">
  <div class="head">SEARCH BY FASHION STYLES</div>
  <div class="label">CHOOSE YOUR CHARACTER</div>
  <div class="select">SELECT YOUR STYLE<span class="caret">▼</span></div>
</div>
<div class="slider-dots abs"><span class="on"></span><span></span><span></span></div>

<section class="brands abs">
  <div class="title">OUR BRANDS:</div>
  <ul><li>Halden</li><li>Solstice</li><li>Comet</li><li>Lunaria</li><li>Ares</li><li>Solstice</li></ul>
</section>

<!-- style tiles -->
<div class="tile" style="left:183px;top:593px;width:244px;height:581px">
  <div class="ph" role="img" aria-label="Woman in a black belted dress" style="background:linear-gradient(180deg,#e9e9e9,#3a3a3a 55%,#1a1a1a)"></div>
  <div class="lbl sm light" style="left:80px;top:340px;text-align:center">Bon Chic<br>Bon Genre</div>
</div>
<div class="tile" style="left:427px;top:593px;width:337px;height:292px">
  <div class="ph" role="img" aria-label="Woman in a white tank top and jeans" style="background:linear-gradient(90deg,#9b9b9b,#c9c6c2 60%,#ddd)"></div>
  <div class="lbl sm light" style="left:86px;top:135px">Casual Collections</div>
</div>
<div class="tile" style="left:764px;top:593px;width:436px;height:292px">
  <div class="ph" role="img" aria-label="Woman in a green bohemian dress with a long necklace" style="background:linear-gradient(90deg,#f3efe8,#e8dcc8 45%,#2f5a3f 80%,#3a6b4a)"></div>
  <div class="lbl sm dark" style="left:36px;top:135px">Bohemian<br>Collections</div>
</div>
<div class="tile" style="left:427px;top:885px;width:469px;height:426px">
  <div class="ph" role="img" aria-label="Woman in a red dress on a city street" style="background:linear-gradient(180deg,#5a5a5a,#3a3a3a 60%,#4a3330)"></div>
  <div class="overlay"></div>
  <div class="chic-mark"><div class="disc"></div><div class="lbl light" style="position:static;white-space:nowrap">Chic Collections</div></div>
</div>
<div class="tile" style="left:896px;top:885px;width:304px;height:170px">
  <div class="ph" role="img" aria-label="Woman in a white blouse" style="background:linear-gradient(90deg,#e6e2dc,#c8c0b5)"></div>
  <div class="lbl light" style="left:160px;top:116px">Boho-Chic</div>
</div>
<div class="tile" style="left:896px;top:1055px;width:304px;height:256px">
  <div class="ph" role="img" aria-label="Woman in a dark puffer jacket among trees" style="background:linear-gradient(90deg,#4c5a45,#2b2b2b 60%,#3a3330)"></div>
  <div class="lbl light" style="left:34px;top:174px">Winter<br>Collection</div>
</div>
<div class="tile" style="left:183px;top:1174px;width:244px;height:325px">
  <div class="ph" role="img" aria-label="Blonde woman in a blue strapless formal dress" style="background:linear-gradient(180deg,#f4f4f4,#d9d9d9 40%,#3a5a8a 75%,#e8e8e8)"></div>
  <div class="lbl dark vert" style="left:196px;top:36px">F<br>O<br>R<br>M<br>A<br>L</div>
</div>
<div class="tile" style="left:183px;top:1499px;width:244px;height:251px">
  <div class="ph" role="img" aria-label="Person in black streetwear and cap" style="background:linear-gradient(90deg,#6f6f6f,#222 50%,#8a8a8a)"></div>
  <div class="lbl light" style="left:70px;top:200px">Streetwear</div>
</div>
<div class="tile" style="left:427px;top:1311px;width:773px;height:439px">
  <div class="ph" role="img" aria-label="Woman with purple hair and sunglasses in a sunflower print dress at a festival" style="background:linear-gradient(90deg,#b7c2b0,#d9c9a2 35%,#c49a3c 50%,#d5d7cc 70%,#bfc6cc)"></div>
  <div class="lbl light" style="left:572px;top:335px">Festival Chic<br>Collections</div>
</div>
<div class="tile" style="left:183px;top:1750px;width:253px;height:266px">
  <div class="ph" role="img" aria-label="Woman in a black sports top and shorts" style="background:linear-gradient(90deg,#fafafa,#e4e4e4 50%,#f2f2f2)"></div>
  <div class="lbl dark" style="left:10px;top:106px">Sporty</div>
</div>
<div class="tile" style="left:436px;top:1750px;width:256px;height:266px">
  <div class="ph" role="img" aria-label="Woman in a classic black dress with pearl necklace" style="background:linear-gradient(90deg,#f1efec,#6a6a6a 45%,#efedea)"></div>
  <div class="lbl dark" style="left:146px;top:212px">Classic</div>
</div>
<div class="tile" style="left:692px;top:1750px;width:257px;height:266px">
  <div class="ph" role="img" aria-label="Accessories: sunglasses, keychain, red clutch and belt" style="background:radial-gradient(ellipse at 50% 70%,#e7c9c9,#ffffff 60%)"></div>
  <div class="lbl dark" style="left:46px;top:24px">Accessories</div>
</div>
<div class="tile" style="left:949px;top:1750px;width:251px;height:605px">
  <div class="ph" role="img" aria-label="Woman in a leopard print lace dress" style="background:linear-gradient(180deg,#f5f5f5 10%,#c7b9a8 40%,#5a4838 70%,#3a2e25)"></div>
  <div class="lbl dark" style="left:20px;top:88px">Sassy</div>
</div>
<div class="tile" style="left:183px;top:2016px;width:381px;height:339px">
  <div class="ph" role="img" aria-label="Woman in a white summer dress by the sea" style="background:linear-gradient(90deg,#e9edf0,#f4f4f4 40%,#5aa7c9 70%,#8cc7de)"></div>
  <div class="lbl dark vert" style="left:30px;top:86px">S<br>U<br>M<br>M<br>E<br>R</div>
</div>
<div class="tile" style="left:564px;top:2016px;width:385px;height:339px">
  <div class="ph" role="img" aria-label="Woman in street chic outfit on a city sidewalk" style="background:linear-gradient(180deg,#6a6a6a,#3d3d3d)"></div>
  <div class="overlay"></div>
  <div class="lbl light" style="left:0;width:385px;top:72px;text-align:center">Street Chic<br>Collections</div>
  <div class="lbl light" style="left:0;width:385px;top:142px;text-align:center;font-size:10px">Sed ut perspiciatis unde omnis iste nat</div>
  <div class="zoom" style="left:160px;top:186px">
    <svg width="64" height="64" viewBox="0 0 64 64" aria-hidden="true"><circle cx="29" cy="29" r="10" fill="none" stroke="#fff" stroke-width="3"/><line x1="36" y1="36" x2="44" y2="44" stroke="#fff" stroke-width="3.5" stroke-linecap="round"/><line x1="25" y1="29" x2="33" y2="29" stroke="#fff" stroke-width="2"/><line x1="29" y1="25" x2="29" y2="33" stroke="#fff" stroke-width="2"/></svg>
  </div>
</div>
<div class="tile" style="left:183px;top:2355px;width:683px;height:443px">
  <div class="ph" role="img" aria-label="Woman in a white office shirt in a bright room" style="background:linear-gradient(90deg,#dfe3e0,#eef0ee 30%,#7a5a48 45%,#f5f5f5 60%,#dcdcdc)"></div>
  <div class="lbl dark" style="left:500px;top:140px;text-align:right;width:150px">Office<br>Collection</div>
</div>
<div class="tile" style="left:866px;top:2355px;width:334px;height:256px">
  <div class="ph" role="img" aria-label="Woman in a dark embroidered jacket on a busy street" style="background:linear-gradient(90deg,#9a9a9a,#2a2a2a 50%,#8b7c5c)"></div>
  <div class="lbl light" style="left:12px;top:14px">Normcore</div>
</div>
<div class="tile" style="left:866px;top:2611px;width:334px;height:429px">
  <div class="ph" role="img" aria-label="Woman in a grey sweater and black skirt holding a clutch" style="background:linear-gradient(90deg,#bfe0ec,#8a8a8a 45%,#c8e5ef)"></div>
  <div class="lbl dark" style="left:174px;top:92px">Preppy<br>Collection</div>
</div>
<div class="tile" style="left:183px;top:2798px;width:244px;height:242px">
  <div class="ph" role="img" aria-label="Woman in a black hat and blue jacket" style="background:linear-gradient(90deg,#2e4a9a,#6a6a6a 55%,#cfcfcf)"></div>
  <div class="lbl dark" style="left:138px;top:46px">Hipster</div>
</div>
<div class="tile" style="left:427px;top:2798px;width:439px;height:242px">
  <div class="ph" role="img" aria-label="Woman in a grey vintage dress" style="background:linear-gradient(90deg,#e4dfe1,#6e6464 35%,#e6e1e2 55%,#e9e5e6)"></div>
  <div class="lbl dark" style="left:260px;top:84px">Vintage<br>Collection</div>
</div>

<section class="promo-editors abs">Editors<br>Picks</section>
<section class="promo-specials abs">Specials</section>
<section class="about abs">
  <div class="disc"></div>
  <div class="name">Velvet Lane</div>
  <h3>About Velvet Lane</h3>
  <p>Lorem ipsum dolor sit amet, consectetur adipiscing elit. Maecenas pellentesque justo ac velit facilisis convallis vel id nisi. Morbi hendrerit ac tellus eu luctus. Vestibulum ullamcorper.</p>
</section>

<footer class="footer abs">
  <div class="fcol" style="left:66px"><h4>Information</h4>
    <ul><li>Home</li><li>Blog</li><li>About</li><li>Editors Pick</li><li>Specials</li><li>My Wardrobe</li></ul></div>
  <div class="fcol" style="left:284px"><h4>Categories</h4>
    <ul><li>Bohemian</li><li>Preppy</li><li>Boho Chic</li><li>Preppy</li><li>Street Chic</li><li>Bon Chic Bon Genre</li><li>Vintage</li></ul></div>
  <div class="fcol" style="left:545px"><h4>Our Products</h4>
    <ul><li>Streetwear</li><li>Winter</li><li>My Wishlist</li><li>Accessories</li><li>All Products</li></ul></div>
  <div class="fcol contact" style="left:794px"><h4>Contacts</h4>
    <ul>
      <li><svg width="12" height="14" viewBox="0 0 12 14"><path d="M6 0a5 5 0 0 0-5 5c0 4 5 9 5 9s5-5 5-9a5 5 0 0 0-5-5z" fill="#bbb"/><circle cx="6" cy="5" r="1.8" fill="#000"/></svg><span>14 Linden Row, Harbour District,<br>Portvale 2040</span></li>
      <li><svg width="12" height="12" viewBox="0 0 12 12"><path d="M2 0l3 3-1.5 1.8a8 8 0 0 0 3.7 3.7L9 7l3 3-2 2C5 12 0 7 0 2z" fill="#bbb"/></svg><span>+44 555 0142 118<br>+44 555 0178 204</span></li>
      <li><svg width="13" height="10" viewBox="0 0 13 10"><rect width="13" height="10" fill="#bbb"/><path d="M0 0l6.5 5L13 0" fill="none" stroke="#000" stroke-width="1.2"/></svg><span>hello@velvetlane.example</span></li>
    </ul></div>
  <div class="copyright abs">© 2014 Velvet Lane Wardrobe all rights are reserved. Privacy Policy | Terms of Use</div>
  <div class="social-foot abs"><span></span><span></span><span></span><span></span><span></span><span class="red"></span></div>
</footer>

</body>
</html>
```